Create Direct Mail Flyer For House Painting Company

The flyer needs to promote "Free Cheese For A Season" (When they paint their whole house. We want to Focus on the offer, also a free colour consultation, the awards and the guarantees! This will be a full colour 2 sided letter box drop flyer.
This is an emotional Direct Response flyer. I want the Headline to be Bold and stand out. Follow the branding if the website https://larkwoodresurfacing.com.au/
I have attached some social media photos to show you the promotion idea of Free Cheese For A Season. Use better photos if you have them.
I have given you a number of photos to use on the brochure, use your skills to determine what you feel is best to use. Also with the Colour consultation points use small photos to emphasise the points.
Have the testimonials and the team photo on the back.
Also have urgency. ACT NOW -OFFER ENDING SOON!

Target Market(s)

Home Owners

Industry/Entity Type

House Painting, Roof Painting

Colors
0054AA
0677BA
7BADD7
CADEEF
E8F1F8

Requirements
Must have
• Keep the Brand Colours. I have attached a sample flyer that shows a concept that I like. Have the testimonials on the back of the flyer. I do not want the flyer to look to busy.

```html
<!DOCTYPE html>
<html lang="en">
<head>
<meta charset="utf-8">
<title>Larkwood Resurfacing – Free Cheese For A Season Flyer</title>
<link href="https://fonts.googleapis.com/css2?family=Bebas+Neue&family=Montserrat:wght@500;600;700;800&display=swap" rel="stylesheet">
<style>
  :root {
    --brand-deep: #0054AA;
    --brand-mid: #0677BA;
    --brand-soft: #7BADD7;
    --brand-pale: #CADEEF;
    --brand-mist: #E8F1F8;
    --slate: #5d686e;
    --slate-light: #dfe3e6;
    --ink: #2e3338;
    --stage: #d3e3f2;
    --white: #ffffff;
    --gold: #c9a84a;
  }
  * { box-sizing: border-box; margin: 0; padding: 0; }
  html, body { width: 708px; height: 1200px; overflow: hidden; }
  body { background: var(--stage); font-family: "Montserrat", Arial, sans-serif; color: var(--ink); position: relative; }

  .page { position: absolute; left: 124px; width: 460px; height: 595px; background: var(--brand-mist); overflow: hidden; box-shadow: 0 2px 8px rgba(0,40,90,.18); }
  .page--front { top: 3px; background: var(--white); }
  .page--back { top: 602px; }

  .display { font-family: "Bebas Neue", "Oswald", sans-serif; font-weight: 400; letter-spacing: .2px; }

  /* ---------- FRONT ---------- */
  .hero-photo { position: absolute; left: 230px; top: 0; width: 230px; height: 214px;
    background: linear-gradient(90deg, rgba(255,255,255,1) 0%, rgba(255,255,255,0) 28%), linear-gradient(180deg, #b9c2d2 0%, #e9ecf2 45%, #c5ccd4 75%, #8e9aa6 100%); }
  .brand { position: absolute; left: 24px; top: 14px; display: flex; align-items: center; gap: 6px; }
  .brand__mark { width: 12px; height: 12px; background: var(--brand-mid); }
  .brand__name { font-weight: 700; font-size: 13px; color: var(--brand-mid); letter-spacing: .5px; }
  .headline { position: absolute; left: 20px; top: 52px; color: var(--brand-deep); font-size: 56px; line-height: 52px; }
  .headline__sub { position: absolute; left: 22px; top: 177px; font-size: 8.5px; font-weight: 800; color: var(--ink); }
  .band { position: absolute; left: 0; width: 460px; height: 10px; background: var(--brand-deep); }
  .page--front .band { top: 212px; }

  .offer-col { position: absolute; left: 296px; top: 222px; width: 164px; height: 373px; background: var(--slate); }
  .treat-photo { position: absolute; left: 300px; top: 196px; width: 150px; height: 170px; border-radius: 50% 50% 40% 40%;
    background: radial-gradient(circle at 45% 45%, #f3d98a 0%, #e2b94f 45%, #b98a2a 100%); opacity: .9; }
  .burst { position: absolute; left: 318px; top: 262px; width: 100px; height: 100px; }
  .burst__text { position: absolute; left: 318px; top: 278px; width: 100px; text-align: center; color: var(--white); font-size: 17px; line-height: 16px; transform: rotate(-22deg); }
  .grab-box { position: absolute; left: 296px; top: 386px; width: 164px; height: 36px; background: var(--brand-mid); color: var(--white); font-size: 7px; font-weight: 800; line-height: 9px; padding: 5px 10px; }
  .offer-col__title { position: absolute; left: 310px; color: var(--white); font-size: 19px; }
  .offer-list { position: absolute; left: 310px; width: 145px; list-style: none; color: var(--white); font-size: 5.6px; font-weight: 600; line-height: 6.5px; }
  .offer-list li { margin-bottom: 5px; }
  .offer-list li::before { content: "• "; }

  .intro__title { position: absolute; left: 18px; top: 229px; color: var(--brand-deep); font-size: 25px; line-height: 24px; }
  .intro__copy { position: absolute; left: 18px; top: 280px; width: 262px; font-size: 5.8px; font-weight: 700; line-height: 7px; text-align: justify; }
  .steps-bar { position: absolute; left: 0; top: 318px; width: 296px; height: 30px; background: var(--slate-light); padding: 3px 18px; }
  .steps-bar__title { color: var(--brand-deep); font-size: 17px; line-height: 16px; }
  .steps-bar__note { font-size: 5.6px; font-weight: 700; }
  .steps { position: absolute; left: 18px; top: 356px; width: 262px; list-style: none; font-size: 5.6px; line-height: 7px; font-weight: 500; text-align: justify; }
  .steps li { margin-bottom: 7px; }
  .steps strong { display: block; font-weight: 800; font-size: 6.4px; }

  /* ---------- BACK ---------- */
  .team-photo { position: absolute; left: 0; top: 0; width: 460px; height: 223px;
    background: linear-gradient(180deg, #1f4f8e 0%, #2f5f98 35%, #8a9097 62%, #6f757a 100%); }
  .page--back .band { top: 223px; }
  .reviews-frame { position: absolute; top: 264px; width: 136px; height: 200px; border: 1px dashed var(--brand-mid); }
  .review { position: absolute; top: 270px; width: 124px; height: 190px; background: var(--white); border-radius: 6px; padding: 44px 8px 6px; font-size: 4.6px; line-height: 5.6px; box-shadow: 0 1px 3px rgba(0,0,0,.12); }
  .review__initial { position: absolute; top: 245px; width: 62px; height: 62px; border-radius: 50%; background: var(--brand-soft); color: var(--white); font-weight: 800; font-size: 38px; line-height: 62px; text-align: center; }
  .review__name { font-weight: 800; font-size: 6px; margin-bottom: 3px; }
  .review__stars { color: var(--brand-deep); font-size: 7px; letter-spacing: 1px; margin-bottom: 3px; }
  .review p { margin-bottom: 5px; font-weight: 500; }
  .review b { font-weight: 800; }

  .awards-photo { position: absolute; left: 0; top: 483px; width: 74px; height: 112px; background: linear-gradient(180deg, #3a2f2a 0%, #5a4a40 60%, #2a2420 100%); }
  .awards-strip { position: absolute; left: 74px; top: 483px; width: 386px; height: 52px; background: var(--brand-soft); }
  .badge { position: absolute; top: 492px; height: 36px; background: var(--white); border-radius: 2px; }
  .badge--gold { background: linear-gradient(90deg, #fffbe9 0%, #fffbe9 48%, var(--gold) 48%, #e3cb7e 100%); }
  .cta { position: absolute; left: 74px; top: 535px; width: 386px; height: 60px; background: var(--brand-deep); color: var(--white); text-align: center; }
  .cta__phone { font-weight: 800; font-size: 20px; margin-top: 11px; letter-spacing: .3px; }
  .cta__links { font-size: 5.2px; font-weight: 700; margin-top: 7px; display: flex; justify-content: center; gap: 14px; align-items: center; }
  .cta__links svg { width: 6px; height: 6px; vertical-align: -1px; margin-right: 3px; }
</style>
</head>
<body>

<section class="page page--front">
  <div class="hero-photo" role="img" aria-label="Modern white two-storey home at dusk"></div>

  <div class="brand"><span class="brand__mark"></span><span class="brand__name">LARKWOOD RESURFACING</span></div>

  <h1 class="headline display">Free Cheese<br>For A Season</h1>
  <p class="headline__sub">WHEN YOU PAINT YOUR WHOLE HOUSE</p>

  <div class="band"></div>

  <div class="offer-col"></div>
  <div class="treat-photo" role="img" aria-label="Platter of gourmet cheese"></div>

  <svg class="burst" viewBox="0 0 100 100" aria-hidden="true">
    <g fill="#0054AA">
      <rect x="20" y="20" width="60" height="60" transform="rotate(0 50 50)"/>
      <rect x="20" y="20" width="60" height="60" transform="rotate(15 50 50)"/>
      <rect x="20" y="20" width="60" height="60" transform="rotate(30 50 50)"/>
      <rect x="20" y="20" width="60" height="60" transform="rotate(45 50 50)"/>
      <rect x="20" y="20" width="60" height="60" transform="rotate(60 50 50)"/>
      <rect x="20" y="20" width="60" height="60" transform="rotate(75 50 50)"/>
    </g>
    <circle cx="50" cy="50" r="36" fill="none" stroke="#0677BA" stroke-width="1"/>
  </svg>
  <p class="burst__text display">Act Now–<br>Offer<br>Ending<br>Soon!</p>

  <div class="grab-box">GRAB YOUR FREE CHEESE AND COLOUR CONSULTATION WHILE THIS OFFER LASTS.</div>

  <h3 class="offer-col__title display" style="top:430px">Our Services:</h3>
  <ul class="offer-list" style="top:452px">
    <li>ROOF RESTORATION AND PAINTING</li>
    <li>HOUSE PAINTING</li>
    <li>EPOXY FLOORS</li>
  </ul>
  <h3 class="offer-col__title display" style="top:491px">Our Guarantees:</h3>
  <ul class="offer-list" style="top:513px">
    <li>ON TIME GUARANTEE</li>
    <li>WHITE GLOVE CLEANLINESS GUARANTEE</li>
    <li>15 YEAR GUARANTEE</li>
    <li>SATISFACTION GUARANTEE</li>
  </ul>

  <h2 class="intro__title display">Transform Your Home And<br>Savour Free Cheese All Season!</h2>
  <p class="intro__copy">PAINT YOUR WHOLE HOUSE WITH US AND RECEIVE A FREE COLOUR CONSULTATION TO ENSURE THE PERFECT SHADE. PLUS, ENJOY A FINE CHEESE SELECTION ALL SEASON, ON US. OUR SKILLED PAINTERS ARE READY TO TRANSFORM YOUR HOME.</p>

  <div class="steps-bar">
    <h3 class="steps-bar__title display">Four Steps To Bring Your Vision To Life!</h3>
    <p class="steps-bar__note">IT IS IMPORTANT TO SELECT THE CORRECT COLOURS FOR YOUR HOME.</p>
  </div>

  <ol class="steps">
    <li><strong>1. CONSIDER THE MOOD YOU WANT TO CREATE:</strong>THINK ABOUT THE ATMOSPHERE YOU WANT TO EVOKE IN EACH ROOM. DO YOU WANT A CALMING AND RELAXING SPACE, OR A VIBRANT AND ENERGIZING ONE? CHOOSE COLOURS THAT ALIGN WITH THE MOOD YOU WANT TO CREATE.</li>
    <li><strong>2. LOOK AT THE ROOM'S NATURAL LIGHT:</strong>TAKE NOTE OF THE AMOUNT AND DIRECTION OF NATURAL LIGHT IN EACH ROOM. LIGHT AFFECTS HOW COLOURS APPEAR, SO YOU'LL WANT TO CHOOSE SHADES THAT COMPLEMENT THE LIGHTING. FOR EXAMPLE, WARM HUES LIKE RED AND ORANGE WORK WELL IN ROOMS WITH A LOT OF NATURAL LIGHT, WHILE COOL HUES LIKE BLUE AND GREEN ARE BETTER SUITED FOR ROOMS WITH LESS LIGHT.</li>
    <li><strong>3. THINK ABOUT THE ROOM'S FUNCTION:</strong>CONSIDER THE PURPOSE OF EACH ROOM AND CHOOSE COLOURS THAT ALIGN WITH THE FUNCTION. FOR INSTANCE, BLUE OR GREEN MAY BE SUITABLE FOR A BEDROOM TO CREATE A CALMING ENVIRONMENT, WHILE YELLOW OR ORANGE MAY WORK WELL IN A KITCHEN TO ADD WARMTH AND ENERGY.</li>
    <li><strong>4. TEST THE COLOURS:</strong>ONCE YOU'VE NARROWED DOWN YOUR CHOICES, TEST THEM OUT IN THE ROOM. PAINT A SMALL PATCH ON THE WALL AND OBSERVE HOW IT LOOKS AT DIFFERENT TIMES OF THE DAY AND IN DIFFERENT LIGHTING CONDITIONS. THIS WILL HELP YOU DETERMINE IF THE COLOUR IS RIGHT FOR THE SPACE.</li>
  </ol>
</section>

<section class="page page--back">
  <div class="team-photo" role="img" aria-label="Painting team standing in front of their branded depot and work vehicles"></div>
  <div class="band"></div>

  <div class="reviews-frame" style="left:8px"></div>
  <div class="reviews-frame" style="left:162px"></div>
  <div class="reviews-frame" style="left:316px"></div>

  <article class="review" style="left:14px">
    <div class="review__name">MAREN HOLLOWAY</div>
    <div class="review__stars">★★★★★</div>
    <p><b>POSITIVE:</b> PROFESSIONALISM, PUNCTUALITY, QUALITY, RESPONSIVENESS, VALUE.</p>
    <p>MOST PROFESSIONAL PAINTERS WE HAVE EVER DEALT WITH. PRECISE WORK, TIDY CREWS AND A RELIABLE COMPANY THAT FOLLOWED UP ON EVERY DETAIL. HIGHLY RECOMMEND THEM TO ANYONE.</p>
    <p><b>SERVICES:</b> INTERIOR PAINTING, EXTERIOR PAINTING</p>
  </article>
  <article class="review" style="left:168px">
    <div class="review__name">TAVI R</div>
    <div class="review__stars">★★★★★</div>
    <p>REPAIRED AND SEALED OUR ROOF AND REPAINTED THE WATER STAINED CEILINGS. FAST QUOTE, QUICK TURNAROUND AND THE TEAM FINISHED AHEAD OF SCHEDULE. GREAT COMMUNICATION AND A PRICE WE WERE HAPPY WITH.</p>
  </article>
  <article class="review" style="left:322px">
    <div class="review__name">COLIN ASHBY</div>
    <div class="review__stars">★★★★★</div>
    <p><b>POSITIVE:</b> PROFESSIONALISM, PUNCTUALITY, QUALITY, RESPONSIVENESS, VALUE.</p>
    <p>NEIL OSTROW AND HIS TEAM ARE TRUE PROFESSIONALS. THEY PAINTED OUR INTERIOR AND EXTERIOR, AND THE RESULT LOOKS BRAND NEW. BEST PAINT TEAM WE HAVE USED AND WE WOULD HAPPILY BOOK THEM AGAIN.</p>
    <p><b>SERVICES:</b> INTERIOR PAINTING, EXTERIOR PAINTING</p>
  </article>

  <div class="review__initial" style="left:45px">M</div>
  <div class="review__initial" style="left:199px">T</div>
  <div class="review__initial" style="left:353px">C</div>

  <div class="awards-photo" role="img" aria-label="Team members at an industry awards night"></div>
  <div class="awards-strip"></div>
  <div class="badge badge--gold" style="left:88px; width:156px"></div>
  <div class="badge" style="left:256px; width:88px"></div>
  <div class="badge" style="left:356px; width:88px"></div>

  <div class="cta">
    <div class="cta__phone">CALL US NOW ON 1300 555 018</div>
    <div class="cta__links">
      <span><svg viewBox="0 0 10 10"><circle cx="5" cy="5" r="4" fill="none" stroke="#fff" stroke-width="1.2"/><path d="M1 5h8M5 1c2 2 2 6 0 8M5 1c-2 2-2 6 0 8" fill="none" stroke="#fff" stroke-width=".8"/></svg>https://larkwoodresurfacing.com.au/</span>
      <span><svg viewBox="0 0 10 10"><rect x="1" y="2" width="8" height="6" fill="none" stroke="#fff" stroke-width="1.2"/><path d="M1 2l4 3.5L9 2" fill="none" stroke="#fff" stroke-width="1"/></svg>admin@larkwoodresurfacing.com.au</span>
    </div>
  </div>
</section>

</body>
</html>
```